I need a wordpress website for myconsulting company specialized in data privacy

I'm looking for a wordpress website for my consulting company specialized in data privacy (GDPR) and computer science.
The website will serve as entry point to for potential clients.
The website should have the following sections (I'm opened to new ideas):
- Presentation of the company
- General presentation
- Services provided with some details
- Blog/articles with tags (if possible)
- Contact
On every page of the website there should be some references to pages (such as privacy policy, legal information...)
If possible he website should be multinlingual (english and french). I'll personnally take care of the translation in french.
Regarding branding;
- Name of the company: Étienne Roubaud Conseil
- Logo is attached
- For colors to be used see attached PDF for exemple

```html
<!DOCTYPE html>
<html lang="en">
<head>
<meta charset="utf-8">
<title>Étienne Roubaud Conseil — Personal Data Protection Compliance Consultancy</title>
<link href="https://fonts.googleapis.com/css2?family=Saira:wght@500;600;700&family=Open+Sans:wght@400;600;700&display=swap" rel="stylesheet">
<style>
:root{
  --teal:#138b9b;
  --teal-light:#6fd3df;
  --navy:#1d3b55;
  --navy-deep:#14283b;
  --footer:#283848;
  --ink:#2c2f33;
  --text:#55595e;
  --muted:#8b9096;
  --line:#d9dde1;
  --paper:#ffffff;
  --mist:#f3f4f6;
}
*{box-sizing:border-box;margin:0;padding:0}
html,body{width:1200px;height:4723px;overflow:hidden}
body{font-family:"Open Sans",Arial,sans-serif;color:var(--text);background:var(--paper);position:relative;font-size:13px;line-height:1.55}
.abs{position:absolute}
h1,h2,h3,.display{font-family:"Saira",Arial,sans-serif;color:var(--ink);font-weight:600}
.eyebrow{font-size:12px;color:var(--teal);font-weight:600}
.section-title{font-size:34px;letter-spacing:.5px;line-height:1.1;text-transform:uppercase}
.lead{font-weight:700;color:var(--ink);font-size:14px;line-height:1.6}
.link-arrow{color:var(--teal);font-family:"Saira",Arial,sans-serif;font-weight:600;font-size:15px;display:flex;align-items:center;gap:14px}
.photo{position:absolute}

/* header */
.site-header{position:absolute;left:0;top:0;width:1200px;height:100px;z-index:3}
.top-bar{position:absolute;left:370px;top:0;width:830px;height:20px;background:var(--navy-deep)}
.top-bar .social{position:absolute;left:74px;top:5px;display:flex;gap:12px}
.dot{width:9px;height:9px;border-radius:50%;background:#cfe3ea;display:block}
.top-bar .phone{position:absolute;left:290px;top:2px;color:#dbe6ee;font-size:10px}
.top-bar .search{position:absolute;left:490px;top:2px;width:212px;height:16px;background:#1e4a66;color:#9fb6c6;font-size:10px;padding-left:12px;line-height:16px}
.nav-band{position:absolute;left:0;top:0;width:1200px;height:73px;background:var(--paper);clip-path:polygon(0 0,395px 0,395px 20px,1200px 20px,1200px 73px,0 73px)}
.brand{position:absolute;left:112px;top:18px;display:flex;align-items:center;gap:10px}
.brand .mark{width:34px;height:34px;border:3px solid var(--teal)}
.brand .name{font-family:"Saira",Arial,sans-serif;font-weight:600;font-size:17px;color:var(--navy)}
.main-nav{position:absolute;top:38px;left:0;width:1200px;font-family:"Open Sans",sans-serif;font-size:12px;color:var(--ink)}
.main-nav span{position:absolute}
.lang{position:absolute;left:1046px;top:37px;font-size:11px;color:var(--ink)}
.header-cut{position:absolute;left:0;top:0}

/* hero */
.hero{position:absolute;left:0;top:0;width:1200px;height:617px;background:linear-gradient(100deg,#2a6b80 0%,#1c8394 45%,#1792a2 70%,#3f7c88 100%)}
.hero .frame{position:absolute;left:352px;top:222px;width:496px;height:268px;border:1px solid rgba(255,255,255,.25)}
.hero h1{position:absolute;left:0;width:1200px;top:256px;text-align:center;color:#fff;font-size:45px;line-height:58px;font-weight:600;letter-spacing:.5px}
.hero p{position:absolute;left:0;width:1200px;top:383px;text-align:center;color:#eaf6f8;font-size:16px;line-height:23px}
.btn-solid{position:absolute;background:var(--teal);color:#fff;font-family:"Saira",Arial,sans-serif;font-weight:600;font-size:16px;display:flex;align-items:center;justify-content:center}

/* about */
.about-visual{left:172px;top:725px;width:371px;height:345px;border-radius:30px;background:linear-gradient(135deg,#1c7a8b,#2b5369 60%,#1a8e9e)}
.about-text{left:613px;top:720px;width:420px}
.rule{width:110px;height:2px;background:var(--teal-light);margin:8px 0 20px}
.about-text p{font-size:12px;margin-bottom:16px;color:var(--text)}
.about-text b{color:var(--ink)}

/* services */
.services{position:absolute;left:0;top:1178px;width:1200px;height:630px;background:linear-gradient(90deg,#f5f6f8 0%,#eff1f4 60%,#e4e8ec 100%)}
.service-card{position:absolute;top:305px;width:222px;height:209px;background:#fff;border:1px solid var(--line);padding:70px 22px 0}
.service-card .icon{position:absolute;left:19px;top:-37px;width:74px;height:74px;background:var(--teal)}
.service-card h3{font-size:18px;margin-bottom:10px}
.service-card p{font-size:10.5px;line-height:1.6}
.circle-btn{position:absolute;width:60px;height:60px;border-radius:50%;display:flex;align-items:center;justify-content:center}

/* what we do */
.specialization{position:absolute;left:0;top:1808px;width:1200px;height:978px;background:var(--mist)}
.center{text-align:center;width:1200px;left:0}
.btn-outline{position:absolute;border:1.5px solid var(--teal);color:var(--teal);font-family:"Saira",Arial,sans-serif;font-weight:600;font-size:15px;display:flex;align-items:center;justify-content:center;gap:14px;background:transparent}
.feature-title{display:flex;align-items:center;gap:14px;font-family:"Saira",Arial,sans-serif;font-weight:600;font-size:18px;color:var(--ink)}
.stat-card{position:absolute;background:#fff;box-shadow:0 6px 18px rgba(0,0,0,.15)}

/* cases */
.case-caption{position:absolute;left:371px;top:3233px;width:464px;height:88px;background:var(--navy-deep);clip-path:polygon(40px 0,100% 0,calc(100% - 40px) 100%,0 100%);padding:14px 0 0 64px;color:#fff}

/* news */
.news-item{position:absolute;left:613px;width:471px;height:82px;display:flex;align-items:flex-start;padding:14px 0 0 18px}
.news-item .day{font-family:"Saira",Arial,sans-serif;font-weight:600;font-size:38px;line-height:1;color:var(--ink);width:62px;margin-top:8px}
.news-item .date{font-size:11px;line-height:1.3;width:48px;margin-top:6px;border-right:1px solid var(--line);height:56px}
.news-item .body{padding-left:18px}
.news-item h4{font-size:12px;color:var(--ink);font-weight:700}
.news-item p{font-size:10.5px;margin:4px 0}
.news-item .more{font-size:11px;color:var(--teal)}

/* contact */
.contact{position:absolute;left:0;top:3900px;width:1200px;height:513px;background:linear-gradient(90deg,#5b6f84 0%,#35536e 25%,#1f4563 45%,#173a58 100%)}
.field{position:absolute;border-bottom:1px solid rgba(255,255,255,.45);color:#c9d6e0;font-size:11px;padding-bottom:8px}

/* footer */
.site-footer{position:absolute;left:0;top:4413px;width:1200px;height:310px;background:var(--footer);color:#d5dde4}
.site-footer h5{font-size:12px;font-weight:700;color:#fff;letter-spacing:.3px}
.site-footer ul{list-style:none}
.site-footer li{font-size:11px;height:26px}
.site-footer li::before{content:"»";margin-right:14px;color:#aab6c0}
</style>
</head>
<body>

<!-- HERO -->
<section class="hero" role="img" aria-label="Photo of consultants working together at a desk, tinted teal">
  <div class="frame"></div>
</section>
<h1 class="abs" style="left:0;width:1200px;top:256px;text-align:center;color:#fff;font-size:45px;line-height:58px">PERSONAL DATA PROTECTION<br>COMPLIANCE CONSULTANCY</h1>
<p class="abs" style="left:0;width:1200px;top:383px;text-align:center;color:#eaf6f8;font-size:16px;line-height:23px">We specialized in data privacy (GDPR) and<br>computer science.</p>
<div class="btn-solid" style="left:499px;top:461px;width:202px;height:53px">Get Started Now</div>

<!-- HEADER -->
<header class="site-header">
  <div class="nav-band"></div>
  <div class="top-bar">
    <div class="social"><i class="dot"></i><i class="dot"></i><i class="dot"></i><i class="dot"></i></div>
    <div class="phone">&#9743; 555-014-2280</div>
    <div class="search">Search here...</div>
  </div>
  <svg class="header-cut" width="1200" height="120" viewBox="0 0 1200 120">
    <path d="M0 105 H330 L396 20" fill="none" stroke="#1d3b55" stroke-width="2"/>
    <path d="M0 112 H336 L402 26" fill="none" stroke="#6fd3df" stroke-width="1" opacity=".6"/>
  </svg>
  <div class="brand"><span class="mark"></span><span class="name">Étienne Roubaud Conseil</span></div>
  <nav class="main-nav">
    <span style="left:535px">HOME</span>
    <span style="left:622px">ABOUT</span>
    <span style="left:716px">SERVICES</span>
    <span style="left:821px">BLOG</span>
    <span style="left:905px">CONTACT US</span>
  </nav>
  <div class="lang">&#9680; En ▾</div>
</header>

<!-- ABOUT -->
<div class="photo about-visual" role="img" aria-label="Photo of two colleagues reviewing work on a laptop"></div>
<div class="abs about-text">
  <div class="eyebrow">About</div>
  <h2 class="section-title" style="margin-top:4px">Who We Are</h2>
  <div class="rule"></div>
  <p class="lead" style="font-size:13.5px">Et ornare viverra magna maecenas amet. Vel viverra pulvinar eu eget malesuada ullamcorper viverra.</p>
  <p><b>OUR MISSION:</b> sit amet, consectetur adipiscing elit. Lorem quisque urna, et commodo erat.</p>
  <p><b>OUR VISSION:</b> sit amet, consectetur adipiscing elit. Lorem quisque urna, et commodo erat. Et ornare viverra magna maecenas amet. Vel viverra pulvinar eu eget malesuada ullamcorper viverra. Turpis pulvinar id integer interdum nulla egestas. Laoreet elit aliquam arcu, sit mauris, arcu ullamcorper ut nunc.</p>
  <div class="link-arrow" style="margin-top:24px">Learn More About <svg width="28" height="10"><path d="M0 5H26M21 1L26 5L21 9" stroke="#138b9b" fill="none" stroke-width="1.5"/></svg></div>
</div>

<!-- SERVICES -->
<section class="services">
  <div class="abs" style="left:640px;top:60px;width:560px;height:460px;background:linear-gradient(120deg,rgba(255,255,255,0),rgba(210,216,222,.6));" role="img" aria-label="Faint photo of a monitor displaying charts"></div>
  <div class="abs eyebrow" style="left:116px;top:82px">Services</div>
  <h2 class="abs section-title" style="left:116px;top:104px">Services We Provide</h2>
  <div class="abs" style="left:116px;top:165px;width:270px;height:1px;background:var(--teal-light)"></div>
  <p class="abs lead" style="left:116px;top:185px;width:410px;font-size:13.5px">Et ornare viverra magna maecenas amet. Vel viverra pulvinar eu eget malesuada ullamcorper viverra.</p>
  <div class="circle-btn" style="left:942px;top:150px;border:1.5px solid var(--teal)"><svg width="28" height="12"><path d="M28 6H2M7 1L2 6L7 11" stroke="#138b9b" fill="none" stroke-width="1.5"/></svg></div>
  <div class="circle-btn" style="left:1025px;top:150px;background:var(--teal)"><svg width="28" height="12"><path d="M0 6H26M21 1L26 6L21 11" stroke="#fff" fill="none" stroke-width="1.5"/></svg></div>

  <div class="service-card" style="left:116px"><div class="icon"><svg width="74" height="74"><circle cx="33" cy="32" r="12" stroke="#fff" fill="none" stroke-width="2"/><path d="M42 41L52 51" stroke="#fff" stroke-width="3"/></svg></div><h3>Service 1</h3><p>Et ornare viverra magna maecenas amet. <b>Vel viverra pulvinar eu</b> eget malesuada ullamcorper viverra.</p></div>
  <div class="service-card" style="left:363px"><div class="icon"><svg width="74" height="74"><rect x="34" y="18" width="22" height="16" stroke="#fff" fill="none" stroke-width="2"/><circle cx="29" cy="38" r="6" stroke="#fff" fill="none" stroke-width="2"/><path d="M18 56V50Q29 42 40 50V56Z" stroke="#fff" fill="none" stroke-width="2"/></svg></div><h3>Service 2</h3><p>Et ornare viverra magna maecenas amet. <b>Vel viverra pulvinar eu</b> eget malesuada ullamcorper viverra.</p></div>
  <div class="service-card" style="left:613px"><div class="icon"><svg width="74" height="74"><path d="M37 16L54 22V36Q54 50 37 58Q20 50 20 36V22Z" stroke="#fff" fill="none" stroke-width="2"/><path d="M29 37L35 43L46 31" stroke="#fff" fill="none" stroke-width="2"/></svg></div><h3>Service 3</h3><p>Et ornare viverra magna maecenas amet. <b>Vel viverra pulvinar eu</b> eget malesuada ullamcorper viverra.</p></div>
  <div class="service-card" style="left:862px"><div class="icon"><svg width="74" height="74"><rect x="18" y="18" width="38" height="28" stroke="#fff" fill="none" stroke-width="2"/><circle cx="37" cy="32" r="6" stroke="#fff" fill="none" stroke-width="2"/><path d="M30 56H44M37 46V56" stroke="#fff" stroke-width="2"/></svg></div><h3>Service 4</h3><p>Et ornare viverra magna maecenas amet. <b>Vel viverra pulvinar eu</b> eget malesuada ullamcorper viverra.</p></div>
</section>

<!-- WHAT WE DO -->
<section class="specialization">
  <div class="abs center eyebrow" style="top:68px">Specialization</div>
  <h2 class="abs center section-title" style="top:98px">What We Do</h2>
  <p class="abs" style="left:300px;top:158px;width:600px;text-align:center;font-size:12px">Et ornare viverra magna maecenas amet. Vel viverra pulvinar eu eget malesuada ullamcorper viverra. Turpis pulvinar id integer interdum nulla egestas. Laoreet elit aliquam arcu, sit mauris, arcu ullamcorper ut nunc.</p>

  <div class="abs feature-title" style="left:172px;top:270px"><svg width="40" height="32"><circle cx="14" cy="12" r="7" stroke="#138b9b" fill="none" stroke-width="1.6"/><path d="M2 30Q14 18 26 30" stroke="#138b9b" fill="none" stroke-width="1.6"/><circle cx="30" cy="22" r="8" stroke="#138b9b" fill="none" stroke-width="1.6"/></svg>Privacy Audit</div>
  <p class="abs" style="left:172px;top:320px;width:420px;font-size:12px">Et ornare viverra magna maecenas amet. <b style="color:var(--ink)">Vel viverra pulvinar eu</b> eget malesuada ullamcorper viverra. Turpis pulvinar id integer interdum nulla egestas.</p>
  <p class="abs" style="left:176px;top:403px;width:420px;font-size:12px">Laoreet elit aliquam arcu, sit mauris, <b style="color:var(--ink)">arcu ullamcorper ut nunc</b>.</p>
  <div class="btn-outline" style="left:172px;top:449px;width:180px;height:46px">Learn More <svg width="28" height="10"><path d="M0 5H26M21 1L26 5L21 9" stroke="#138b9b" fill="none" stroke-width="1.5"/></svg></div>

  <div class="abs" style="left:840px;top:242px;width:188px;height:270px;background:var(--teal-light)"></div>
  <div class="photo" style="left:657px;top:254px;width:358px;height:268px;background:linear-gradient(135deg,#e9edf0,#b9c2c9 60%,#7b8590)" role="img" aria-label="Photo of analysts working at computers showing charts"></div>
  <div class="stat-card" style="left:629px;top:456px;width:136px;height:90px">
    <div class="abs" style="left:8px;top:6px;font-size:6px;color:var(--muted)">Compensation</div>
    <div class="abs" style="left:85px;top:8px;font-size:11px;color:var(--ink)">14,750</div>
    <svg class="abs" style="left:8px;top:38px" width="120" height="44"><path d="M0 40L0 28Q15 12 28 26T56 22T84 10T120 26V40Z" fill="#3fb9c8"/><path d="M0 40L0 34Q20 22 40 32T80 26T120 34V40Z" fill="#138b9b"/></svg>
  </div>

  <div class="abs" style="left:172px;top:589px;width:186px;height:270px;background:var(--teal-light)"></div>
  <div class="photo" style="left:185px;top:601px;width:358px;height:266px;background:linear-gradient(135deg,#c9d1d8,#8a97a3 55%,#e8ecef)" role="img" aria-label="Photo of two colleagues reviewing a laptop dashboard"></div>
  <div class="stat-card" style="left:433px;top:805px;width:136px;height:90px">
    <svg class="abs" style="left:14px;top:10px" width="110" height="42"><circle cx="20" cy="20" r="16" stroke="#e3e8ec" stroke-width="5" fill="none"/><circle cx="20" cy="20" r="16" stroke="#138b9b" stroke-width="5" fill="none" stroke-dasharray="75 101" transform="rotate(-90 20 20)"/><circle cx="82" cy="20" r="16" stroke="#e3e8ec" stroke-width="5" fill="none"/><circle cx="82" cy="20" r="16" stroke="#6fd3df" stroke-width="5" fill="none" stroke-dasharray="45 101" transform="rotate(-90 82 20)"/></svg>
    <div class="abs" style="left:16px;top:58px;font-size:6px;color:var(--muted)">Received</div>
    <div class="abs" style="left:84px;top:58px;font-size:6px;color:var(--muted)">Pending</div>
    <div class="abs" style="left:16px;top:68px;font-size:10px;color:var(--teal)">14,750</div>
    <div class="abs" style="left:84px;top:68px;font-size:10px;color:var(--teal-light)">125K</div>
  </div>

  <div class="abs feature-title" style="left:613px;top:614px"><svg width="40" height="36"><rect x="2" y="16" width="16" height="14" stroke="#138b9b" fill="none" stroke-width="1.6"/><circle cx="30" cy="10" r="6" stroke="#138b9b" fill="none" stroke-width="1.6"/><path d="M20 32Q30 18 40 32" stroke="#138b9b" fill="none" stroke-width="1.6"/><rect x="6" y="2" width="14" height="10" stroke="#138b9b" fill="none" stroke-width="1.6"/></svg>Privacy Advice</div>
  <p class="abs" style="left:617px;top:672px;width:430px;font-size:12px">Laoreet elit aliquam arcu, sit mauris, <b style="color:var(--ink)">arcu ullamcorper ut nunc</b>.</p>
  <p class="abs" style="left:613px;top:714px;width:430px;font-size:12px">Et ornare viverra magna maecenas amet. <b style="color:var(--ink)">Vel viverra pulvinar eu</b> eget malesuada ullamcorper viverra. Turpis pulvinar id integer interdum nulla egestas.</p>
  <div class="btn-outline" style="left:613px;top:799px;width:180px;height:48px">Learn More <svg width="28" height="10"><path d="M0 5H26M21 1L26 5L21 9" stroke="#138b9b" fill="none" stroke-width="1.5"/></svg></div>
</section>

<!-- CASE STUDIES -->
<div class="abs center eyebrow" style="top:2878px">Projects</div>
<h2 class="abs center section-title" style="top:2905px">Our Case Studies</h2>
<div class="photo" style="left:0;top:2985px;width:314px;height:294px;background:linear-gradient(135deg,#9aa5ae,#d8dee3 55%,#7d8a95)" role="img" aria-label="Photo of a team meeting around a table"></div>
<div class="photo" style="left:339px;top:2985px;width:522px;height:294px;background:linear-gradient(135deg,#aab4bc,#dfe4e8 50%,#88949e)" role="img" aria-label="Photo of colleagues discussing a project at a meeting"></div>
<div class="photo" style="left:886px;top:2985px;width:314px;height:294px;background:linear-gradient(135deg,#8f9ba5,#d3d9de 55%,#a3adb5)" role="img" aria-label="Photo of a team meeting around a table"></div>
<div class="case-caption">
  <div style="font-family:'Saira',sans-serif;font-weight:600;font-size:16px">Laoreet elit aliquam arcu, sit mauris</div>
  <div style="font-size:10.5px;line-height:1.6;width:300px;margin-top:4px;color:#dfe7ee">Et ornare viverra magna maecenas amet. <b>Vel viverra pulvinar eu</b> eget malesuada ullamcorper</div>
</div>
<svg class="abs" style="left:371px;top:3280px" width="470" height="48"><path d="M315 32H342" stroke="#fff" stroke-width="1.5"/><path d="M337 28L342 32L337 36" stroke="#fff" fill="none" stroke-width="1.5"/><path d="M0 44H420L462 0" stroke="#138b9b" fill="none" stroke-width="3"/></svg>

<!-- LATEST NEWS -->
<div class="abs eyebrow" style="left:116px;top:3556px">Blog</div>
<h2 class="abs section-title" style="left:116px;top:3582px">Latest News</h2>
<p class="abs" style="left:116px;top:3650px;width:380px;font-size:12px">Et ornare viverra magna maecenas amet. Vel viverra pulvinar eu eget malesuada ullamcorper viverra. Turpis pulvinar id integer interdum nulla egestas</p>
<div class="abs link-arrow" style="left:116px;top:3728px">View All News <svg width="28" height="10"><path d="M0 5H26M21 1L26 5L21 9" stroke="#138b9b" fill="none" stroke-width="1.5"/></svg></div>

<article class="news-item" style="top:3450px"><div class="day">20</div><div class="date">feb<br>2022</div><div class="body"><h4>Arcu Ullamcorper Ut Nunc</h4><p>Ornare viverra magna maecenast. Turpis pulvinar...</p><div class="more">Read More &nbsp;⟶</div></div></article>
<article class="news-item" style="top:3547px;height:105px;background:#fff;box-shadow:0 4px 18px rgba(0,0,0,.1);border-left:3px solid var(--teal);padding-top:24px"><div class="day" style="color:var(--teal)">20</div><div class="date" style="color:var(--teal)">feb<br>2022</div><div class="body"><h4>Arcu Ullamcorper Ut Nunc</h4><p>Ornare viverra magna maecenast. Turpis pulvinar...</p><div class="more">Read More &nbsp;⟶</div></div></article>
<article class="news-item" style="top:3660px"><div class="day">20</div><div class="date">feb<br>2022</div><div class="body"><h4>Arcu Ullamcorper Ut Nunc</h4><p>Ornare viverra magna maecenast. Turpis pulvinar...</p><div class="more">Read More &nbsp;⟶</div></div></article>
<article class="news-item" style="top:3744px"><div class="day">20</div><div class="date">feb<br>2022</div><div class="body"><h4>Arcu Ullamcorper Ut Nunc</h4><p>Ornare viverra magna maecenast. Turpis pulvinar...</p><div class="more">Read More &nbsp;⟶</div></div></article>

<!-- CONTACT -->
<section class="contact">
  <div class="abs" style="left:0;top:0;width:560px;height:513px;background:linear-gradient(90deg,rgba(220,226,232,.55),rgba(120,140,160,.25) 60%,rgba(23,58,88,0))" role="img" aria-label="Photo of two businessmen looking at a tablet"></div>
  <div class="abs" style="left:613px;top:72px;font-size:12px;color:#dbe6ee">Blog</div>
  <h2 class="abs section-title" style="left:613px;top:98px;color:#fff">Contact Us</h2>
  <p class="abs" style="left:613px;top:163px;color:#fff;font-weight:700;font-size:13.5px">Et ornare viverra magna maecenas amet.</p>
  <div class="field" style="left:613px;top:228px;width:224px;height:21px">Name *</div>
  <div class="field" style="left:861px;top:228px;width:223px;height:21px">Company Name *</div>
  <div class="field" style="left:613px;top:280px;width:471px;height:22px">Email *</div>
  <div class="field" style="left:613px;top:333px;width:471px;height:50px">How Can We Help You?</div>
  <div class="btn-solid" style="left:613px;top:410px;width:125px;height:50px">Submit</div>
</section>

<!-- FOOTER -->
<footer class="site-footer">
  <svg class="abs" style="left:0;top:0" width="560" height="150"><path d="M120 138H400L528 12H600" stroke="#4a5d6f" fill="none" stroke-width="1.5"/></svg>
  <div class="abs" style="left:123px;top:58px;display:flex;align-items:center;gap:10px"><span style="width:30px;height:30px;border:3px solid #fff;display:block"></span><span style="font-family:'Saira',sans-serif;font-weight:600;font-size:17px;color:#fff">Étienne Roubaud Conseil</span></div>
  <div class="abs" style="left:176px;top:190px;display:flex;gap:24px"><i class="dot" style="width:14px;height:14px"></i><i class="dot" style="width:14px;height:14px"></i><i class="dot" style="width:14px;height:14px"></i><i class="dot" style="width:14px;height:14px"></i></div>

  <h5 class="abs" style="left:591px;top:60px">QUICK LINKS</h5>
  <ul class="abs" style="left:591px;top:93px"><li>Home</li><li>About</li><li>Services</li><li>Blog</li><li>Contact Us</li></ul>
  <h5 class="abs" style="left:756px;top:60px">OTHER LINKS</h5>
  <ul class="abs" style="left:756px;top:93px"><li>Site Map</li><li>Privacy Policy</li><li>Privacy Security</li><li>careers</li></ul>
  <h5 class="abs" style="left:923px;top:60px">CONTACT US</h5>
  <div class="abs" style="left:923px;top:106px;font-size:11.5px;display:flex;gap:10px"><svg width="12" height="16"><path d="M6 15Q0 8 0 6A6 6 0 0 1 12 6Q12 8 6 15Z" fill="#6fd3df"/><circle cx="6" cy="6" r="2" fill="#283848"/></svg><span>418 Harbor Lane, Milford,<br>Ohio 45150</span></div>
  <div class="abs" style="left:923px;top:154px;font-size:11.5px;display:flex;gap:10px"><svg width="14" height="14"><path d="M2 1L5 1L6 5L4 6Q6 9 8 10L9 8L13 9V12Q13 13 12 13Q1 12 1 2Q1 1 2 1Z" fill="#6fd3df"/></svg><span>555-014-2280</span></div>

  <div class="abs" style="left:116px;top:232px;width:968px;height:1px;background:#43566a"></div>
  <div class="abs center" style="top:272px;font-size:10.5px;color:#c3ccd4">Copyright 2022, <u>Étienne Roubaud Conseil</u> | All Rights Reserved</div>
</footer>

</body>
</html>
```